Collection of baby & child print designs.

We require a collection of designs that can be edited and customised in Adobe Illustrator/InDesign so that they can be personalised for our customers.

The designs can be of anything, but must include a child's name, date of birth, or location of birth (basically any personal identifier) or a combination of the above.

A range of examples of similar products can be found here - http://lnk.vorbey.net/8Qtrw

Our designs can take influence from the examples on this site, but must be different.

We require a range of options for both boys and girls.
Updates

Reason: For amends to be made to some designs.

Target Market(s)

Parents, Friends of parents, people looking for a unique gift.

Industry/Entity Type

Baby

Requirements
Must have
• Must fit within the printable area of an A3 page.

```html
<!DOCTYPE html>
<html lang="en">
<head>
<meta charset="utf-8">
<title>Alfie – Birth Mobile Print</title>
<link rel="stylesheet" href="https://fonts.googleapis.com/css2?family=Oswald:wght@700&family=Sniglet:wght@800&family=Rye&family=Stardos+Stencil:wght@700&family=Playball&display=swap">
<style>
  :root {
    --sky: #bddcf7;
    --paper: #ffffff;
    --star-white: #f8f9fb;
    --bow-tint: #d9ebfb;
    --ink-blue: #a9d5f8;
  }
  html, body {
    margin: 0;
    padding: 0;
    width: 846px;
    height: 1200px;
    overflow: hidden;
    background: var(--sky);
  }
  .print {
    display: block;
    width: 846px;
    height: 1200px;
  }
  .string { stroke: var(--paper); stroke-width: 3; fill: none; }
  .rail { stroke: var(--paper); stroke-linecap: round; fill: none; }
  .tag, .bauble { fill: var(--paper); }
  .ring-hole { fill: var(--sky); }

  .name-cloud-area { fill: var(--paper); }
  .bow-area { fill: var(--bow-tint); }
  .star-area { fill: var(--star-white); }

  .child-name {
    font-family: "Oswald", "Arial Narrow", sans-serif;
    font-weight: 700;
    font-size: 140px;
    fill: var(--ink-blue);
  }
  .label-birth {
    font-family: "Sniglet", "Arial Rounded MT Bold", sans-serif;
    font-weight: 800;
    font-size: 33px;
    fill: var(--ink-blue);
  }
  .birth-date {
    font-family: "Stardos Stencil", "Stencil", serif;
    font-weight: 700;
    font-size: 76px;
    fill: var(--paper);
  }
  .label-weight {
    font-family: "Rye", "Rockwell", serif;
    font-size: 64px;
    fill: var(--ink-blue);
  }
  .weight-value {
    font-family: "Playball", "Brush Script MT", cursive;
    font-size: 33px;
    fill: var(--ink-blue);
  }
  .star-sign {
    font-family: "Oswald", "Arial Narrow", sans-serif;
    font-weight: 700;
    font-size: 44px;
    fill: var(--ink-blue);
  }
</style>
</head>
<body>
<svg class="print" viewBox="0 0 846 1200" xmlns="http://www.w3.org/2000/svg">
  <!-- Name cloud -->
  <rect class="name-cloud-area" x="200" y="115" width="468" height="265" rx="60"
        role="img" aria-label="Scalloped cloud with small stars around the edge, holding the child's name"/>
  <text class="child-name" x="434" y="292" text-anchor="middle">Alfie</text>

  <!-- Mobile frame -->
  <line class="string" x1="433" y1="380" x2="433" y2="843"/>
  <line class="rail" x1="126" y1="450" x2="742" y2="450" stroke-width="10"/>

  <!-- Date of birth arm -->
  <line class="string" x1="246" y1="450" x2="246" y2="760"/>
  <circle class="tag" cx="246" cy="570" r="12"/><circle class="ring-hole" cx="246" cy="570" r="4"/>
  <rect class="tag" x="88" y="580" width="309" height="60" rx="7"/>
  <text class="label-birth" x="242" y="623" text-anchor="middle">date of birth</text>
  <circle class="tag" cx="246" cy="757" r="12"/><circle class="ring-hole" cx="246" cy="757" r="4"/>
  <line class="rail" x1="80" y1="771" x2="410" y2="771" stroke-width="9"/>
  <text class="birth-date" x="245" y="832" text-anchor="middle">12.02.13</text>

  <!-- Weight arm -->
  <line class="string" x1="631" y1="450" x2="631" y2="530"/>
  <circle class="tag" cx="631" cy="530" r="12"/><circle class="ring-hole" cx="631" cy="530" r="4"/>
  <rect class="tag" x="467" y="541" width="328" height="99" rx="7"/>
  <text class="label-weight" x="628" y="622" text-anchor="middle">WEIGHT</text>
  <line class="string" x1="568" y1="640" x2="568" y2="740"/>
  <line class="string" x1="706" y1="640" x2="706" y2="730"/>
  <circle class="bauble" cx="568" cy="778" r="47"/>
  <circle class="ring-hole" cx="568" cy="743" r="4"/>
  <circle class="bauble" cx="704" cy="772" r="48"/>
  <circle class="ring-hole" cx="705" cy="737" r="4"/>
  <text class="weight-value" x="567" y="789" text-anchor="middle">8lb</text>
  <text class="weight-value" x="704" y="783" text-anchor="middle">10oz</text>

  <!-- Ribbon bow -->
  <rect class="bow-area" x="356" y="656" width="136" height="86" rx="10"
        role="img" aria-label="White ribbon bow tied on the centre string"/>

  <!-- Star sign -->
  <rect class="star-area" x="287" y="843" width="298" height="283" rx="12"
        role="img" aria-label="Large white five-pointed star hanging from the mobile"/>
  <text class="star-sign" x="443" y="988" text-anchor="middle">Aquarius</text>
</svg>
</body>
</html>
```